Lucky Orbit Fun Casino Entertainment

Looking to update my business card and make it look more modern, stand out and eye catching.
We are are fun casino business in Australia (primarily Sydney). Blackjack and Roulette are our most popular games although we have pretty much every game available for hire that you would find in a real casino. The final design would need to be sleek and appeal to the more upmarket corporate sector.
We mainly cater for Corporate Events, Private Parties, Fundraising Events, Team Building, Poker Tournaments
I think I'd prefer the colour Black.

Target Market(s)

High-end Corporate

Industry/Entity Type

Events

Contact Information for Business Card

Dale Hutchins
Director
1300 482 617
0431 758 209
info@luckyorbit.com.au
www.luckyorbit.com.au
Facebook & Instagram @luckyorbitshows (proper social icons preferred)

Colors
000000
0255a3

Requirements
Must have
• Front side:
• Logo
• Contact details
• 'Australia's #1 Fun Casino Specialists'
• Back:
• Logo
Nice to have
• Back:
• Corporate Events
• Private Parties
• Poker Tournaments
• Fundraising
• Props & Theming
• Photo Booth
• Horse Racing Events
• The Vegas Sign attached, maybe on the back of the card in the background...?

```html
<!DOCTYPE html>
<html lang="en">
<head>
<meta charset="utf-8">
<title>Lucky Orbit – Business Card</title>
<link rel="stylesheet" href="https://fonts.googleapis.com/css2?family=Montserrat:wght@600&family=Lato:wght@400&display=swap">
<style>
  :root {
    --page-bg: #2b2b2b;
    --card-bg: #222222;
    --accent: #f5a623;
    --text: #f2f2f2;
    --sign-light: #fff4c8;
    --sign-mid: #e9b949;
    --sign-deep: #a0621c;
  }
  * { box-sizing: border-box; margin: 0; padding: 0; }
  html, body { width: 1200px; height: 1200px; overflow: hidden; }
  body { background: var(--page-bg); position: relative; font-family: "Lato", sans-serif; color: var(--text); }

  .card {
    position: absolute; left: 187px; width: 825px; height: 470px;
    background: var(--card-bg); overflow: hidden;
    box-shadow: 0 14px 30px rgba(0,0,0,.55);
  }
  .card--front { top: 86px; }
  .card--back { top: 640px; }

  .brand { position: absolute; display: flex; align-items: center; gap: 14px; }
  .brand__dot { width: 64px; height: 64px; border-radius: 50%; background: var(--accent); flex: none; }
  .brand__name { font-family: "Montserrat", sans-serif; font-weight: 600; font-size: 34px; color: var(--accent); white-space: nowrap; }
  .card--front .brand { left: 470px; top: 114px; }
  .card--back .brand { left: 48px; top: 104px; }

  .person { position: absolute; left: 47px; top: 192px; }
  .person__name { font-family: "Montserrat", sans-serif; font-weight: 600; font-size: 30px; color: var(--accent); line-height: 1; text-transform: uppercase; }
  .person__role { font-size: 19px; margin-top: 6px; }

  .contact { position: absolute; left: 47px; list-style: none; font-size: 19px; }
  .contact li { display: flex; align-items: center; gap: 8px; height: 27px; }
  .contact svg { width: 16px; height: 16px; flex: none; }
  .contact--social { top: 273px; }
  .contact--social .social-dot { width: 20px; height: 20px; border-radius: 50%; background: var(--accent); margin-right: 2px; }
  .contact--details { top: 325px; }

  .tagline { position: absolute; right: 46px; top: 403px; font-size: 19px; }

  .services { position: absolute; left: 47px; top: 258px; list-style: none; font-size: 19px; line-height: 23.3px; }

  .sign-photo {
    position: absolute; left: 437px; top: 0; width: 388px; height: 470px;
    background: radial-gradient(ellipse 60% 58% at 62% 50%, var(--sign-light) 0%, var(--sign-mid) 38%, var(--sign-deep) 70%, var(--card-bg) 100%);
  }
</style>
</head>
<body>
  <section class="card card--front">
    <div class="brand"><span class="brand__dot"></span><span class="brand__name">Lucky Orbit</span></div>

    <div class="person">
      <h1 class="person__name">Dale Hutchins</h1>
      <p class="person__role">Director</p>
    </div>

    <ul class="contact contact--social">
      <li><span class="social-dot"></span>@luckyorbitshows</li>
    </ul>

    <ul class="contact contact--details">
      <li><svg viewBox="0 0 16 16"><path fill="var(--accent)" d="M3.6 1.5l2.3 2.6-1.3 1.8c.8 1.9 2.3 3.4 4.2 4.3l1.8-1.3 2.6 2.3-1.4 2.3C6.6 13.3 2.7 9.4 1.3 4.2z"/></svg>0431 758 209</li>
      <li><svg viewBox="0 0 16 16"><path fill="var(--accent)" d="M3.6 1.5l2.3 2.6-1.3 1.8c.8 1.9 2.3 3.4 4.2 4.3l1.8-1.3 2.6 2.3-1.4 2.3C6.6 13.3 2.7 9.4 1.3 4.2z"/></svg>1300 482 617</li>
      <li><svg viewBox="0 0 16 16"><rect x="1" y="3.5" width="14" height="9" fill="var(--accent)"/><path d="M1 3.5l7 5 7-5" fill="none" stroke="var(--card-bg)" stroke-width="1.3"/></svg>info@luckyorbit.com.au</li>
      <li><svg viewBox="0 0 16 16"><g fill="none" stroke="var(--accent)" stroke-width="1.2"><circle cx="8" cy="8" r="6.5"/><ellipse cx="8" cy="8" rx="3" ry="6.5"/><path d="M1.5 8h13M2.5 4.8h11M2.5 11.2h11"/></g></svg>www.luckyorbit.com.au</li>
    </ul>

    <p class="tagline">Australia's #1 Fun Casino Specialists</p>
  </section>

  <section class="card card--back">
    <div class="sign-photo" role="img" aria-label="Photo of a glowing illuminated welcome sign of a famous casino city"></div>
    <div class="brand"><span class="brand__dot"></span><span class="brand__name">Lucky Orbit</span></div>
    <ul class="services">
      <li>- Corporate Events</li>
      <li>- Private Parties</li>
      <li>- Poker Tournaments</li>
      <li>- Fundraising</li>
      <li>- Props &amp; Theming</li>
      <li>- Photo Booth</li>
      <li>- Horse Racing Events</li>
    </ul>
  </section>
</body>
</html>
```